9x12 Business Brochure, 3 fold, for Internet Marketing Company

I'd like to have a brochure designed for my Internet marketing company. I have the content all ready, 10 Internet Marketing Myths, which you can see here: http://www.steadfernwebreach.com/common-internet-marketing-myths/. I'm looking for something creative and business to business. The company is all about Internet marketing. I like the "http://" header I use at our website. People like it too and identify with it. Audience is business owners 35 to 55 years old. I use blue at my website. I *think* I would like the cover page (front page) to open with some attention grabbing text, that basically takes most of the front page of the brochure. It would probably say: "I Can Help You Get BETTER RESULTS from Your Website, More Traffic, TOP RANKINGS at Zorvik, More Leads and MORE SALES. But first you'll have to avoid these common Internet marketing myths..." The inside pages would have the content from above (the 10 myths). The back page would have testimonials that I can provide. And the inside folded in page (or what I call the inside folded in page) would have a list of services. I think I want the dimensions 12x9 which is a larger sized, three-fold brochure.

Target Market(s)

I use this brochure to send to business owners and managers to show them I know what I'm talking about and and expert. See attachment for content.

Industry/Entity Type

Marketing

Requirements
Should not have
• No clipart. Probably not illustrations. Photos. The "http://" used at the site is something people "connect" with and get that this is about Internet marketing.

```html
<!DOCTYPE html>
<html lang="en">
<head>
<meta charset="utf-8">
<title>Steadfern Web Reach – Tri-fold Brochure</title>
<link rel="stylesheet" href="https://fonts.googleapis.com/css2?family=Arimo:ital,wght@0,400;0,700;1,400&display=swap">
<style>
  :root {
    --slate: #5d6c79;
    --slate-dark: #46545f;
    --slate-light: #8a97a3;
    --navy: #0e2a5c;
    --navy-mid: #1b3c73;
    --navy-soft: #2d4f85;
    --globe-blue: #2f7fc8;
    --white: #ffffff;
    --ink-light: #e8eef5;
  }
  * { box-sizing: border-box; margin: 0; padding: 0; }
  html, body { width: 1200px; height: 901px; overflow: hidden; background: #ececec; }
  body { font-family: "Arimo", Arial, sans-serif; color: var(--white); }

  .brochure { position: relative; width: 1200px; height: 901px; display: flex; }
  .panel { position: relative; width: 400px; height: 901px; overflow: hidden; }

  /* Services panel */
  .panel--services { background: linear-gradient(180deg, var(--slate) 0%, var(--slate-dark) 100%); }
  .services-title { position: absolute; left: 60px; top: 14px; font-size: 34px; font-weight: 700; line-height: 1.3; }
  .services-box {
    position: absolute; left: 0; top: 104px; width: 379px; height: 708px;
    border-radius: 0 10px 10px 0;
    background: linear-gradient(90deg, var(--navy-mid) 0%, var(--navy-soft) 55%, var(--navy) 100%);
  }
  .services-list { position: absolute; left: 24px; top: 38px; list-style: none; }
  .services-list li { font-size: 18px; line-height: 30.9px; padding-left: 20px; position: relative; }
  .services-list li::before {
    content: ""; position: absolute; left: 0; top: 11px; width: 8px; height: 8px; background: var(--ink-light);
  }
  .services-quote {
    position: absolute; left: 0; width: 379px; top: 628px; text-align: center;
    font-size: 18px; font-style: italic; line-height: 30px;
  }
  .services-call { position: absolute; left: 0; width: 379px; top: 842px; text-align: center; font-size: 23px; font-weight: 700; }

  /* Back panel */
  .panel--back { background: var(--white); }
  .back-visual {
    position: absolute; left: 0; top: 0; width: 400px; height: 172px;
    background: radial-gradient(ellipse at 50% 100%, var(--globe-blue) 0%, #8cc0e8 45%, var(--white) 75%);
  }
  .back-body {
    position: absolute; left: 0; top: 172px; width: 400px; height: 729px;
    background: linear-gradient(90deg, var(--navy-mid) 0%, var(--navy) 100%);
    padding: 12px 27px 0 28px;
  }
  .stories-title { font-size: 40px; font-weight: 700; text-align: center; margin-bottom: 10px; margin-left: -14px; }
  .story { font-size: 13.4px; line-height: 20px; text-align: justify; margin-bottom: 19px; }
  .story strong { font-size: 16.5px; }
  .back-sign { position: absolute; left: 0; width: 400px; top: 648px; text-align: center; font-size: 18px; font-weight: 700; line-height: 24px; }

  /* Front panel */
  .panel--front { background: linear-gradient(180deg, var(--slate-light) 0%, var(--slate) 60%, var(--slate-dark) 100%); }
  .front-visual {
    position: absolute; left: 0; top: 0; width: 400px; height: 480px;
    background: radial-gradient(circle at 28% 18%, var(--globe-blue) 0%, #1d4f8e 22%, transparent 40%),
                linear-gradient(160deg, #14305e 0%, #5f7e9c 35%, #c7d2db 60%, var(--slate-light) 100%);
  }
  .front-brand {
    position: absolute; left: 0; width: 400px; top: 220px; text-align: center;
    font-size: 38px; font-weight: 700; color: var(--ink-light); line-height: 46px;
  }
  .front-headline {
    position: absolute; left: 0; width: 400px; top: 494px; text-align: center;
    font-weight: 700; line-height: 29px; font-size: 23px;
  }
  .front-headline .big { font-size: 31px; }
  .front-cta {
    position: absolute; left: 0; top: 724px; width: 400px; height: 177px;
    border-radius: 12px 0 0 0;
    background: linear-gradient(90deg, var(--navy-mid) 0%, var(--navy) 100%);
    text-align: center; padding-top: 26px;
  }
  .front-cta .myths { font-size: 20px; line-height: 25px; }
  .front-cta .firm { font-size: 18px; font-weight: 700; margin-top: 18px; }
  .front-cta .phone { font-size: 25px; font-weight: 700; margin-top: 4px; }
</style>
</head>
<body>
<main class="brochure">
  <section class="panel panel--services">
    <h2 class="services-title">Services &amp;<br>Expertise</h2>
    <div class="services-box">
      <ul class="services-list">
        <li>Internet Strategy Development</li>
        <li>Custom Website Design</li>
        <li>Blog Design &amp; Support</li>
        <li>Online Marketing Copywriting</li>
        <li>Social Media Marketing</li>
        <li>Search Engine Optimization (SEO)</li>
        <li>Conversion Optimization</li>
        <li>Content Marketing Management</li>
        <li>Using Friendbook for Business</li>
        <li>Zorvik+, Streamly, Pinboardly</li>
        <li>Email Marketing &amp; Production</li>
        <li>Inquiry and Lead Development</li>
        <li>Zorvik AdLine Pay-Per-Click</li>
        <li>Zorvik Local Places (maps)</li>
        <li>E-Commerce Development</li>
        <li>High-Performance Hosting</li>
        <li>Security &amp; Contingency Planning</li>
        <li>One-on-One or Group Training</li>
      </ul>
      <p class="services-quote">“If you think it’s expensive to hire an<br>expert,&nbsp; wait until you hire an amateur.”</p>
    </div>
    <p class="services-call">Call Us: (866) 555-0148</p>
  </section>

  <section class="panel panel--back">
    <div class="back-visual" role="img" aria-label="Globe with a browser address bar reading http://www and a pointer cursor"></div>
    <div class="back-body">
      <h2 class="stories-title">Success Stories</h2>
      <p class="story"><strong>Zorvik Rankings</strong> – “… we have spent over a year trying to get onto page one at Zorvik. I has been very frustrating and we’ve wasted a lot of time and money. Dana explained everything very clearly and we did everything he told us. 90 days later we’re now showing up on the first page of Zorvik!</p>
      <p class="story"><strong>Website Design</strong> – “We needed a new website that properly reflected our company and the products and services we sell. We started getting more leads within 72 hours of launching the new site Dana and his team designed for us. We’re also getting better results from our Zorvik AdLine pay-per-click advertising and more of those clicks are turning into inquiries!”</p>
      <p class="story"><strong>More to Come</strong> - Lorem ipsum dolor sit amet, consectetur adipiscing elit. Suspendisse justo velit, auctor ut pulvinar a, egestas non urna. Suspendisse potenti. Sed at pellentesque dolor. Vivamus sed nibh nisl. Nunc tortor tellus, facilisis eget pretium vitae, porttitor quis libero.</p>
      <p class="story"><strong>More to Come</strong> - Lorem ipsum dolor sit amet, consectetur adipiscing elit. Suspendisse justo velit, auctor ut pulvinar a, egestas non urna. Suspendisse potenti. Sed at pellentesque dolor. Vivamus sed nibh nisl. Nunc tortor tellus, facilisis eget pretium vitae, porttitor quis libero.</p>
      <p class="back-sign">DANA WHITLOCK<br>Dana Whitlock Consulting (.com)</p>
    </div>
  </section>

  <section class="panel panel--front">
    <div class="front-visual" role="img" aria-label="Globe circled by an arrow beside an http://www address bar, above large 3D WWW letters and a pointer cursor"></div>
    <p class="front-brand">STEADFERN<br>Web REACH</p>
    <h1 class="front-headline">
      I Can Help You Get<br>
      <span class="big">BETTER RESULTS</span><br>
      from Your Website,<br>
      More Traffic,<br>
      <span class="big">TOP RANKINGS</span> with<br>
      Zorvik, More Inquiries, &amp;<br>
      <span class="big">MORE SALES</span>
    </h1>
    <div class="front-cta">
      <p class="myths">But first you’ll need to avoid these<br>Common Internet Marketing Myths…</p>
      <p class="firm">Dana Whitlock Consulting (.com)</p>
      <p class="phone">(866) 555-0148</p>
    </div>
  </section>
</main>
</body>
</html>
```